The homepage of a website

This is a simple project that should take from you a few minutes as what is needed is the design of the homepage only, the details are in the attached zip file

Please note that KLVTA board required a special tailored design where they got some parts from the different posted designs, if you are interested please follow the instructions in the below URL and submit your new updated designs as per the instructions (P.S. I will mark the project as guaranteed as an assurance to all of you)

http://qorvinworks.example/Projects/KLVTA/Design.jpg
Updates

Please note that KLVTA board required a special tailored design where they got some parts from the different posted designs, if you are interested please follow the instructions in the below URL and submit your new updated designs as per the instructions (P.S. I will mark the project as guaranteed as an assurance to all of you) http://qorvinworks.example/Projects/KLVTA/Design.jpg

```html
<!DOCTYPE html>
<html lang="en">
<head>
<meta charset="utf-8">
<title>KLVTA – Home</title>
<link href="https://fonts.googleapis.com/css2?family=Lato:wght@400;700&family=Ubuntu:wght@400;500&display=swap" rel="stylesheet">
<style>
:root{
  --navy:#1d4a7a;
  --navy-deep:#173f69;
  --orange:#f26a2e;
  --green:#8dc63f;
  --band:#f1f1f1;
  --rule:#dcdcdc;
  --text:#555;
  --dark:#333;
}
*{margin:0;padding:0;box-sizing:border-box}
html,body{width:678px;height:1200px;overflow:hidden;background:#fff}
body{position:relative;font-family:Lato,sans-serif;color:var(--text);font-size:6.6px;line-height:1.55}
.abs{position:absolute}
h2{font-family:Ubuntu,sans-serif;font-weight:400;color:var(--navy);font-size:12px}
.topbar{left:0;top:0;width:678px;height:18px;background:var(--navy)}
.topbar ul{position:absolute;right:69px;top:0;display:flex;list-style:none;height:18px}
.topbar li{color:#fff;font-size:6.5px;line-height:18px;padding:0 8px;border-left:1px solid #2e5e90}
.topbar li.lang{background:var(--navy-deep)}
.brand{left:69px;top:22px;display:flex;align-items:center;gap:6px}
.brand .mark{width:40px;height:40px;border-radius:50%;border:2px solid var(--navy)}
.brand span{font-family:Lato,sans-serif;font-weight:700;font-size:13px;color:var(--navy)}
.society{right:69px;top:30px;width:310px;text-align:right;font-size:11px;color:var(--navy);line-height:1.4}
.nav{left:69px;top:82px;width:541px;height:24px;background:#f4f4f4;border-bottom:1px solid #e3e3e3}
.nav a{position:absolute;top:0;line-height:24px;font-size:6.2px;font-weight:700;color:#333;text-decoration:none}
.nav a.active{background:var(--navy);color:#fff;padding:0 8px;left:0}
.nav .search{position:absolute;left:444px;top:4px;width:73px;height:16px;background:#fff;border:1px solid #e0e0e0;font-size:5.5px;line-height:14px;padding-left:6px;color:#888}
.nav .btn{position:absolute;left:519px;top:4px;width:16px;height:16px;background:var(--orange)}
.hero{left:69px;top:107px;width:541px;height:179px;background:var(--navy)}
.hero .photo{position:absolute;left:255px;top:0;width:286px;height:179px;background:linear-gradient(120deg,#2e6ba0 0%,#9fc8e3 45%,#d9e7ef 100%)}
.hero h1{position:absolute;left:17px;top:55px;width:240px;font-family:Lato,sans-serif;font-weight:400;font-size:14.5px;line-height:21px;color:#fff}
.sec-title{border-bottom:1px solid var(--rule);padding-bottom:3px}
.members{left:69px;top:300px;width:372px}
.members p{margin-top:6px;width:238px;font-size:6.4px;line-height:10.3px}
.members .first{margin-top:8px}
.btn-orange{display:inline-block;background:var(--orange);color:#fff;font-family:Ubuntu,sans-serif;font-weight:500;font-size:9px;padding:2px 13px;margin-top:6px}
.poster{left:318px;top:324px;width:124px;height:139px;background:linear-gradient(160deg,#f6e9d8,#e7c9cf)}
.calendar{left:457px;top:300px;width:153px}
.cal{margin-top:9px;border:1px solid #ddd;height:139px;position:relative}
.cal-head{height:25px;background:var(--orange);color:#fff;font-family:Ubuntu,sans-serif;font-size:10.5px;text-align:center;line-height:25px;position:relative}
.cal-head svg{position:absolute;top:8px}
.cal table{border-collapse:collapse;margin:8px auto 0;font-size:5.3px;color:#444}
.cal td{width:19.8px;height:19.8px;text-align:center}
.cal td.mute{color:#bbb}
.cal td.today span{display:inline-block;background:#555;color:#fff;width:14px;height:14px;line-height:14px}
.band{left:0;width:678px;background:var(--band)}
.feature{position:absolute;top:500px;width:150px;text-align:center}
.feature h3{font-family:Ubuntu,sans-serif;font-weight:500;color:var(--navy);font-size:10.5px;margin-top:7px}
.feature p{font-size:6.3px;line-height:10.3px;margin-top:3px}
.gallery{left:69px;top:654px;width:541px}
.gallery .row{display:flex;gap:6px;margin-top:10px}
.gallery .tile{width:103.4px;height:68px;position:relative}
.gallery .cap{position:absolute;left:0;bottom:0;right:0;height:20px;background:rgba(60,60,60,.75);color:#fff;font-size:7.5px;line-height:20px;padding-left:11px}
.col{position:absolute;top:786px;width:168px}
.col h2{display:flex;align-items:center;gap:6px}
.item{position:relative;height:84px;margin-top:12px}
.item .thumb{position:absolute;left:0;top:0;width:74px;height:64px}
.item .body{position:absolute;left:84px;top:0;width:84px}
.item b{display:block;color:var(--dark);font-size:6.7px;line-height:8.6px}
.meta{color:#888;font-size:5.6px;margin:4px 0 3px}
.item .body p{font-size:6.3px;line-height:10.3px}
.journal b{display:block;color:var(--dark);font-size:6.7px;margin-top:9px}
.journal p.txt{font-size:6.3px;line-height:10.4px}
.partners{left:69px;top:1000px;width:541px;height:44px}
.partners h2{position:absolute;left:0;top:11px;display:flex;gap:6px;align-items:center}
.badge{position:absolute;background:#d7dfe8}
.footer{left:0;top:1065px;width:678px;height:135px;background:var(--navy);color:#fff}
.links{position:absolute;top:19px;list-style:none}
.links li{font-size:6.2px;line-height:14.8px;padding-left:7px;position:relative}
.links li::before{content:"";position:absolute;left:0;top:5px;border-left:3px solid #fff;border-top:2.5px solid transparent;border-bottom:2.5px solid transparent}
.footer h4{font-family:Lato,sans-serif;font-weight:400;font-size:9px;position:absolute}
.news-txt{position:absolute;left:359px;top:38px;width:130px;font-size:6px;line-height:8.6px}
.field{position:absolute;left:359px;top:66px;width:115px;height:17px;background:#fff}
.sub{position:absolute;left:359px;top:93px;width:56px;height:18px;background:var(--green);font-family:Ubuntu,sans-serif;font-weight:500;font-size:9px;text-align:center;line-height:18px}
.social{position:absolute;left:506px;top:39px;display:flex;gap:4px}
.social span{width:16px;height:16px;border-radius:50%;background:#fff}
.legal{position:absolute;left:506px;font-size:6px;line-height:9px}
</style>
</head>
<body>

<div class="abs topbar"><ul><li>Login</li><li>Register</li><li class="lang">English ▾</li></ul></div>

<div class="abs brand"><div class="mark"></div><span>KLVTA</span></div>
<div class="abs society">The Kelvara Society of Plastic<br>&amp; Reconstructive Surgeons</div>

<nav class="abs nav">
  <a class="active" href="#">HOME</a>
  <a style="left:44px" href="#">BOARD</a>
  <a style="left:83px" href="#">HISTORY</a>
  <a style="left:128px" href="#">MEMBERS</a>
  <a style="left:177px" href="#">ACTIVITIES</a>
  <a style="left:227px" href="#">LAWS</a>
  <a style="left:261px" href="#">JOURNAL</a>
  <a style="left:309px" href="#">DOWNLOADS</a>
  <a style="left:369px" href="#">LINKS</a>
  <a style="left:404px" href="#">CONTACT</a>
  <div class="search">Enter Keywords</div>
  <div class="btn"><svg width="16" height="16" viewBox="0 0 16 16"><circle cx="7" cy="7" r="3" fill="none" stroke="#fff" stroke-width="1.3"/><line x1="9.2" y1="9.2" x2="11.5" y2="11.5" stroke="#fff" stroke-width="1.4"/></svg></div>
</nav>

<section class="abs hero">
  <h1>THE KELVARA SOCIETY OF PLASTIC AND RECONSTRUCTIVE SURGEONS..</h1>
  <div class="photo" role="img" aria-label="Surgical team operating under theatre lights"></div>
</section>

<section class="abs members">
  <h2 class="sec-title" style="width:372px">Search KLVTA Members</h2>
  <p class="first">Lorem ipsum dolor sit amet, consectetur adipiscing elit. Morbi blandit facilisis leo, id malesuada mi eleifend vestibulum. Maecenas in tempus tellu consequat, felis egestas varius commodo, nisl quam interdum justo, vitae fermentum arcu nunc sed risus. Sed viverra mollis nibh eget porta. Cras orci just condimentum vel tristique at, accumsan vel ipsum. Nunc vulputate velit nec dui mollis, non facilisis purus pretium. Pellentesque arcu erat, condimentum vel feugiat quis, luctus eget odio. Praesent sapien urna, maximus sit amet.</p>
  <p>Aenean nec magna nec urna luctus egestas interdum et arcu. Duis tincidu urna dolor, quis condimentum diam egestas id. Proin quis egestas erat, ut feugi felis Cras non risus mi. Etiam sit amet malesuada ipsum, quis tincidunt odio Integer ornare auctor lectus a suscipit.</p>
  <span class="btn-orange">Search</span>
</section>
<div class="abs poster" role="img" aria-label="Annual conference poster"></div>

<section class="abs calendar">
  <h2 class="sec-title">Events Calendar</h2>
  <div class="cal">
    <div class="cal-head">
      <svg style="left:10px" width="8" height="9" viewBox="0 0 8 9"><path d="M6 1 2 4.5 6 8" fill="none" stroke="#fff" stroke-width="2"/></svg>
      JANUARY 2015
      <svg style="right:10px" width="8" height="9" viewBox="0 0 8 9"><path d="M2 1 6 4.5 2 8" fill="none" stroke="#fff" stroke-width="2"/></svg>
    </div>
    <table>
      <tr><td class="mute">30</td><td class="mute">31</td><td>1</td><td>2</td><td>3</td><td>4</td><td>5</td></tr>
      <tr><td>6</td><td>7</td><td>8</td><td>9</td><td>10</td><td>11</td><td>12</td></tr>
      <tr><td>13</td><td>14</td><td>15</td><td>16</td><td>17</td><td class="today"><span>18</span></td><td>19</td></tr>
      <tr><td>20</td><td>21</td><td>22</td><td>24</td><td>25</td><td>26</td><td>27</td></tr>
      <tr><td>28</td><td>29</td><td>30</td><td>31</td><td class="mute">1</td><td class="mute">2</td><td class="mute">3</td></tr>
    </table>
  </div>
</section>

<div class="abs band" style="top:483px;height:157px"></div>
<div class="feature" style="left:91px">
  <svg width="70" height="70" viewBox="0 0 70 70"><path d="M44 4a30 30 0 0 1 6 50" fill="none" stroke="var(--navy)" stroke-width="1.3"/><circle cx="31" cy="36" r="22" fill="none" stroke="var(--navy)" stroke-width="3" stroke-dasharray="60 18"/><circle cx="31" cy="36" r="16" fill="#fff" stroke="#ccd" stroke-width=".6"/><rect x="23" y="31" width="16" height="10" fill="none" stroke="var(--navy)" stroke-width="1.5"/><path d="M22 31h18l-9-5z" fill="var(--navy)"/></svg>
  <h3>Universities</h3>
  <p>Lorem ipsum dolor sit amet, consectetur adipiscing elit. Morbi blandit facilisis leo, id malesuada mi eleifend vestibulum.</p>
</div>
<div class="feature" style="left:261px">
  <svg width="70" height="70" viewBox="0 0 70 70"><path d="M44 4a30 30 0 0 1 6 50" fill="none" stroke="var(--navy)" stroke-width="1.3"/><circle cx="31" cy="36" r="22" fill="none" stroke="var(--navy)" stroke-width="3" stroke-dasharray="60 18"/><circle cx="31" cy="36" r="16" fill="#fff" stroke="#ccd" stroke-width=".6"/><rect x="22" y="28" width="18" height="12" rx="1" fill="var(--navy)"/><rect x="20" y="41" width="22" height="2" fill="var(--navy)"/></svg>
  <h3>E-Learning</h3>
  <p>Lorem ipsum dolor sit amet, consectetur adipiscing elit. Morbi blandit facilisis leo, id malesuada mi eleifend vestibulum.</p>
</div>
<div class="feature" style="left:431px">
  <svg width="70" height="70" viewBox="0 0 70 70"><path d="M44 4a30 30 0 0 1 6 50" fill="none" stroke="var(--navy)" stroke-width="1.3"/><circle cx="31" cy="36" r="22" fill="none" stroke="var(--navy)" stroke-width="3" stroke-dasharray="60 18"/><circle cx="31" cy="36" r="16" fill="#fff" stroke="#ccd" stroke-width=".6"/><circle cx="31" cy="28" r="4" fill="var(--navy)"/><path d="M22 43l9-10 9 10z" fill="var(--navy)"/></svg>
  <h3>Patients Education</h3>
  <p>Lorem ipsum dolor sit amet, consectetur adipiscing elit. Morbi blandit facilisis leo, id malesuada mi eleifend vestibulum.</p>
</div>

<section class="abs gallery">
  <h2 class="sec-title" style="display:flex;gap:7px;align-items:center"><svg width="16" height="13" viewBox="0 0 16 13"><rect x="1" y="2" width="14" height="10" fill="none" stroke="var(--navy)" stroke-width="1.5"/><path d="M3 10l4-4 3 3 2-2 2 3z" fill="var(--navy)"/></svg>Gallery</h2>
  <div class="row">
    <div class="tile" role="img" aria-label="Patient being marked before surgery" style="background:linear-gradient(135deg,#c9b7a6,#e7e2dc)"><div class="cap">Consectetur adipisci</div></div>
    <div class="tile" role="img" aria-label="Woman checking skin in a mirror" style="background:linear-gradient(135deg,#b8a08e,#e4d6c8)"></div>
    <div class="tile" role="img" aria-label="Man receiving facial injections" style="background:linear-gradient(135deg,#aebfcc,#dfe6ec)"></div>
    <div class="tile" role="img" aria-label="Face with treatment markings" style="background:linear-gradient(135deg,#d6c2b0,#f1e8e0)"></div>
    <div class="tile" role="img" aria-label="Woman with cosmetic markings" style="background:linear-gradient(135deg,#d7c9c4,#f6f2f0)"></div>
  </div>
</section>

<div class="abs band" style="top:770px;height:209px"></div>
<section class="col" style="left:69px">
  <h2 class="sec-title"><svg width="13" height="13" viewBox="0 0 13 13"><rect x="1" y="2" width="11" height="10" fill="none" stroke="var(--navy)" stroke-width="1.4"/><path d="M1 5h11M4 8h1M7 8h1M10 8h1M4 10h1M7 10h1" stroke="var(--navy)"/></svg>News</h2>
  <div class="item"><div class="thumb" role="img" aria-label="Facial treatment photo" style="background:linear-gradient(135deg,#c9b3a3,#efe5dc)"></div><div class="body"><b>Lorem ipsum dolor sit amet, consectetur</b><div class="meta">Posted by 03 Jan 2015</div><p>Lorem ipsum dolor sit ame consectetur adipiscing elt. Morbi blandit facilisis.</p></div></div>
  <div class="item"><div class="thumb" role="img" aria-label="Skin treatment photo" style="background:linear-gradient(135deg,#d1bba9,#f4ece5)"></div><div class="body"><b>Lorem ipsum dolor sit amet, consectetur</b><div class="meta">Posted by 03 Jan 2015</div><p>Lorem ipsum dolor sit ame consectetur adipiscing elt. Morbi blandit facilisis.</p></div></div>
</section>
<section class="col" style="left:255px">
  <h2 class="sec-title"><svg width="13" height="13" viewBox="0 0 13 13"><rect x="1" y="2" width="11" height="10" fill="none" stroke="var(--navy)" stroke-width="1.4"/><path d="M1 5h11M4 8h1M7 8h1M10 8h1M4 10h1M7 10h1" stroke="var(--navy)"/></svg>Events &amp; Upcoming Events</h2>
  <div class="item"><div class="thumb" role="img" aria-label="Relaxing facial treatment" style="background:linear-gradient(135deg,#6fa4c4,#d8e4ea)"></div><div class="body"><b>Lorem ipsum dolor sit amet, consectetur</b><div class="meta">Posted by 03 Jan 2015</div><p>Lorem ipsum dolor sit ame consectetur adipiscing elt. Morbi blandit facilisis.</p></div></div>
  <div class="item"><div class="thumb" role="img" aria-label="Operating theatre" style="background:linear-gradient(135deg,#3f6f92,#a9c4d4)"></div><div class="body"><b>Lorem ipsum dolor sit amet, consectetur</b><div class="meta">Posted by 03 Jan 2015</div><p>Lorem ipsum dolor sit ame consectetur adipiscing elt. Morbi blandit facilisis.</p></div></div>
</section>
<section class="col journal" style="left:442px">
  <h2 class="sec-title"><svg width="16" height="13" viewBox="0 0 16 13"><path d="M1 12C4 6 9 2 15 1 13 6 8 10 2 12z" fill="var(--navy)"/></svg>KLVTA Journal</h2>
  <b>Publishing Information</b>
  <div class="meta">Posted by 03 Jan 2015</div>
  <p class="txt">Lorem ipsum dolor sit amet, consectetur adipiscing eli Morbi blandit facilisis leo, id malesuada mi eleifend ml vestibulum. Maecenas in tempus tellu consequat, Felis egestas varius commodo, nisl quam interdum justo, od vitae fermentum arcu nunc sed risus. Sed viverra moln is nibh eget porta. Cras orci just condimentum vel trist ique at, accumsan vel ipsum. Nunc vulputate velit neck dui mollis, non facilisis.</p>
  <span class="btn-orange" style="margin-top:10px">View Details</span>
</section>

<section class="abs partners">
  <h2><svg width="16" height="14" viewBox="0 0 16 14"><path d="M1 9l5-6 3 3 4-4 2 2-6 7-3-3-3 3z" fill="var(--navy)"/></svg>Our Partners</h2>
  <div class="badge" style="left:122px;top:0;width:46px;height:46px;border-radius:50%"></div>
  <div class="badge" style="left:193px;top:3px;width:38px;height:38px;border-radius:50%"></div>
  <div class="badge" style="left:255px;top:12px;width:86px;height:20px"></div>
  <div class="badge" style="left:364px;top:0;width:60px;height:44px"></div>
  <div class="badge" style="left:450px;top:12px;width:91px;height:20px"></div>
</section>

<footer class="abs footer">
  <ul class="links" style="left:76px"><li>Home</li><li>About Klvta</li><li>Law &amp; Regulation</li><li>Gallery</li><li>News</li><li>Universities</li><li>Contact Us</li></ul>
  <ul class="links" style="left:159px"><li>Home</li><li>About Klvta</li><li>Law &amp; Regulation</li><li>Gallery</li><li>News</li><li>Universities</li><li>Contact Us</li></ul>
  <ul class="links" style="left:242px"><li>Home</li><li>About Klvta</li><li>Law &amp; Regulation</li><li>Gallery</li><li>News</li><li>Universities</li><li>Contact Us</li></ul>
  <h4 style="left:359px;top:23px">Newsletter Signup</h4>
  <p class="news-txt">Enter your email and subscribe our bio monthly newsletter</p>
  <div class="field"></div>
  <div class="sub">Subscribe</div>
  <h4 style="left:506px;top:23px">Follow us on</h4>
  <div class="social"><span></span><span></span><span></span></div>
  <p class="legal" style="top:66px">Terms &amp; Conditions<br>Privacy Policy</p>
  <p class="legal" style="top:97px">Copyrights © KLVTA 2015<br>by KLVTA.com All right reserveds.</p>
</footer>

</body>
</html>
```